Letterhead Design

I have my company logo, slogan, etc. please refer to attachment for your onward design.

An Overview / Background of the Business & Services – Specialised in high-end boutique interior furnishing and fabricate furniture.

The Target Market / Audience you are trying to reach – Global client to US for high-end brand. 90% of our client are from USA.

Design Specifics; any preferences or ideas for Style, Colour, Imagery, etc – No. We have our own logo and slogan, hence would need design of letterhead, business card, envelopes and complimentary slip, if possible, otherwise letterhead will do.

Industry/Entity Type

Boutique

```html
<!DOCTYPE html>
<html lang="en">
<head>
<meta charset="utf-8">
<title>Crestline Atelier Interiors – Letterhead</title>
<link href="https://fonts.googleapis.com/css2?family=Mulish:wght@400;700&display=swap" rel="stylesheet">
<style>
  :root {
    --backdrop: #ebebeb;
    --paper: #ffffff;
    --brand-brown: #4a3b37;
    --ink: #3a302d;
    --ink-soft: #6b605c;
    --sketch-light: #f4f4f4;
    --sketch-mid: #e6e6e6;
  }
  * { box-sizing: border-box; margin: 0; padding: 0; }
  html, body {
    width: 1200px; height: 1192px; overflow: hidden;
    background: var(--backdrop);
    font-family: "Mulish", Arial, sans-serif;
    color: var(--ink);
  }
  .letterhead {
    position: absolute;
    left: 225px; top: 62px;
    width: 750px; height: 1068px;
    background: var(--paper);
    box-shadow: 0 6px 22px rgba(0,0,0,0.12);
    overflow: hidden;
  }
  .letterhead__spine {
    position: absolute; left: 0; top: 0; bottom: 0;
    width: 22px; background: var(--brand-brown);
  }
  .letterhead__sketch {
    position: absolute; left: 22px; right: 0;
    top: 330px; bottom: 0;
    background: linear-gradient(160deg, var(--paper) 0%, var(--sketch-light) 30%, var(--sketch-mid) 60%, var(--sketch-light) 100%);
  }
  .brand-mark {
    position: absolute; top: 70px; right: 60px;
    display: flex; flex-direction: column; align-items: flex-end; gap: 6px;
  }
  .brand-mark__name {
    display: flex; align-items: center; gap: 10px;
    font-weight: 700; font-size: 19px; letter-spacing: 0.5px;
    color: var(--brand-brown);
  }
  .brand-mark__square {
    width: 18px; height: 18px; background: var(--brand-brown);
  }
  .brand-mark__reg {
    font-size: 8px; letter-spacing: 1px; color: var(--ink-soft);
  }
  .footer {
    position: absolute; left: 52px; right: 52px; bottom: 60px;
    display: flex; align-items: flex-end; justify-content: space-between;
  }
  .footer__company-name {
    font-weight: 700; font-size: 22px; color: var(--ink);
  }
  .footer__address {
    font-size: 12px; color: var(--ink-soft); margin-top: 4px;
  }
  .contact {
    display: flex; gap: 48px; font-size: 13px; color: var(--ink);
  }
  .contact__list { list-style: none; display: flex; flex-direction: column; gap: 4px; }
  .contact__item { display: flex; align-items: center; gap: 7px; }
  .contact__icon { width: 11px; height: 11px; fill: var(--ink); }
</style>
</head>
<body>
  <main class="letterhead">
    <div class="letterhead__spine"></div>
    <div class="letterhead__sketch" role="img" aria-label="Faint grey architectural line sketch of an interior space"></div>

    <header class="brand-mark">
      <div class="brand-mark__name"><span class="brand-mark__square"></span>Crestline Atelier Interiors</div>
      <div class="brand-mark__reg">REG NO 201300000K</div>
    </header>

    <footer class="footer">
      <div class="footer__company">
        <div class="footer__company-name">Crestline Atelier Interiors</div>
        <div class="footer__address">Here is your company long address</div>
      </div>
      <div class="contact">
        <ul class="contact__list">
          <li class="contact__item">
            <svg class="contact__icon" viewBox="0 0 12 12"><rect x="3" y="0.5" width="6" height="11" rx="1"/></svg>
            (000) 000-0000
          </li>
          <li class="contact__item">
            <svg class="contact__icon" viewBox="0 0 12 12"><path d="M2 1l3 0 1 3-2 1c1 2 2 3 3 3l1-2 3 1 0 3c-6 0-9-3-9-9z"/></svg>
            (000) 000-0000
          </li>
        </ul>
        <ul class="contact__list">
          <li class="contact__item">
            <svg class="contact__icon" viewBox="0 0 12 12"><rect x="0.5" y="2.5" width="11" height="7"/></svg>
            yourname@yourwebsite.com
          </li>
          <li class="contact__item">
            <svg class="contact__icon" viewBox="0 0 12 12"><circle cx="6" cy="6" r="5.5"/></svg>
            www.yourwebsite.com
          </li>
        </ul>
      </div>
    </footer>
  </main>
</body>
</html>
```